Poster for our end of year annual dance concert

We need an A3 portrait poster for our end of year concert.
Designs are attached of posters from previous 3 years as a reference only.
The theme of our concert this year is "Comets & Lanterns ".
This is a fun them with dance routines choreographed to songs such as "Glimmerlass", "Fox Maiden", "Zip Lassie", "Quillor", "The Tinker", "Velvet Otters", "Drifters", "Gremlets", etc, etc
Dance styles in the concert include Jazz & Hip Hop.
Bright colors are preferred in the design.

Target Market(s)

Dance school students & their families

Industry/Entity Type

Dance Studio

Font styles to use
Sans Serif

Requirements
Must have
• Size: A3 Portrait
• You will see in the samples from previous years the poster must have:
• The Rosalind Pike Dancers (font is Mistral) + logo (supplied)
• Bellward Theatre
• Marlowe College Fernbrook
• Concert date this year is: Saturday 19th November
• Website: www.rpkdancers-site.com.au
Nice to have
• Clean design, not cluttered with too much imagery

```html
<!DOCTYPE html>
<html lang="en">
<head>
<meta charset="utf-8">
<title>Comets &amp; Lanterns – The Rosalind Pike Dancers</title>
<link rel="stylesheet" href="https://fonts.googleapis.com/css2?family=Bangers&family=Dancing+Script:wght@600&family=Oswald:wght@500;700&display=swap">
<style>
  :root {
    --sky-blue: #1f8fd6;
    --deep-blue: #123f8f;
    --navy: #1a2a5c;
    --white: #ffffff;
    --yellow: #ffd21f;
    --orange: #ff7a1a;
    --magenta: #e6198a;
    --pink: #ff3fa4;
    --cream-yellow: #fff36b;
    --red: #e3262f;
  }
  html, body {
    margin: 0;
    padding: 0;
    overflow: hidden;
    background: var(--deep-blue);
  }
  .poster {
    position: relative;
    width: 853px;
    height: 1200px;
    overflow: hidden;
    background: radial-gradient(circle at 50% 35%, #3fb0ee 0%, var(--sky-blue) 40%, var(--deep-blue) 100%);
    font-family: "Oswald", sans-serif;
  }
  .brand {
    position: absolute;
    top: 16px;
    left: 0;
    width: 100%;
    text-align: center;
    color: var(--white);
    z-index: 3;
  }
  .brand-mark {
    display: block;
    width: 60px;
    height: 60px;
    margin: 0 auto 18px;
    border-radius: 50%;
    background: var(--white);
  }
  .brand-name {
    font-family: "Dancing Script", cursive;
    font-weight: 600;
    font-size: 46px;
    line-height: 1;
  }
  .hero-art {
    position: absolute;
    left: 170px;
    top: 190px;
    width: 570px;
    height: 700px;
    background: linear-gradient(180deg, #d9c3b4 0%, #b8c6df 35%, var(--navy) 75%, #0e1a3d 100%);
    z-index: 1;
  }
  .burst-area {
    position: absolute;
    z-index: 2;
  }
  .burst-left { left: 18px; top: 375px; width: 195px; height: 190px; background: var(--magenta); }
  .burst-right { left: 670px; top: 175px; width: 183px; height: 160px; background: var(--pink); }
  .burst-bottom { left: 290px; top: 900px; width: 563px; height: 300px; background: var(--magenta); }
  .presents {
    position: absolute;
    left: 268px;
    top: 565px;
    padding: 2px 26px;
    background: var(--magenta);
    color: var(--yellow);
    font-family: "Bangers", sans-serif;
    font-size: 44px;
    letter-spacing: 2px;
    transform: rotate(-4deg);
    z-index: 4;
  }
  .title {
    position: absolute;
    left: 200px;
    top: 615px;
    width: 580px;
    margin: 0;
    text-align: center;
    font-family: "Bangers", sans-serif;
    font-weight: 400;
    color: var(--yellow);
    line-height: 0.95;
    transform: rotate(-4deg);
    text-shadow: 5px 5px 0 var(--orange);
    z-index: 4;
  }
  .title-line { display: block; font-size: 150px; }
  .title-amp { display: block; font-size: 70px; line-height: 0.8; color: var(--cream-yellow); }
  .event-info {
    position: absolute;
    left: 370px;
    top: 965px;
    width: 400px;
    text-align: center;
    transform: rotate(-4deg);
    z-index: 4;
  }
  .event-day, .event-date {
    font-family: "Bangers", sans-serif;
    color: var(--cream-yellow);
    line-height: 1;
    text-shadow: 3px 3px 0 var(--navy);
  }
  .event-day { font-size: 46px; }
  .event-date { font-size: 46px; }
  .venue {
    margin-top: 10px;
    color: var(--white);
    font-weight: 700;
    font-size: 24px;
    line-height: 1.15;
    text-transform: uppercase;
  }
  .website {
    position: absolute;
    left: 36px;
    top: 1138px;
    color: var(--red);
    font-size: 20px;
    font-weight: 500;
    z-index: 4;
  }
</style>
</head>
<body>
<main class="poster">
  <header class="brand">
    <span class="brand-mark"></span>
    <div class="brand-name">The Rosalind Pike Dancers</div>
  </header>

  <div class="hero-art" role="img" aria-label="Comic-style superhero illustration"></div>
  <div class="burst-area burst-left" role="img" aria-label="Comic starburst decoration"></div>
  <div class="burst-area burst-right" role="img" aria-label="Comic starburst decoration"></div>
  <div class="burst-area burst-bottom" role="img" aria-label="Comic starburst behind event details"></div>

  <div class="presents">PRESENTS</div>

  <h1 class="title">
    <span class="title-line">COMETS</span>
    <span class="title-amp">&amp;</span>
    <span class="title-line">LANTERNS</span>
  </h1>

  <section class="event-info">
    <div class="event-day">SATURDAY</div>
    <div class="event-date">19TH NOVEMBER 2016</div>
    <div class="venue">Bellward Theatre<br>Marlowe College Fernbrook</div>
  </section>

  <div class="website">www.rpkdancers-site.com.au</div>
</main>
</body>
</html>
```